International Trading Company, 'KIRO' needs a Business Card

The company name is "KIRO" and it has own logo design.
I'd like to use its logo on this business card.
I need two side Business Card.
I'll look forward to your great design.
Thank you very much in advance.

Contact Information for Business Card

Company Name : Kiro Harbour Limited
Information Example
Dorian Pallister
Mobile(use icon please) : 1 (212) 555-0143
Tel(use icon please) : 1 (212) 555-0178
Email(use icon please) : dorian27@kiroharbour-mail.com
Address(use icon please) : 482 Halden Ave, New York, NY 10160, USA

```html
<!DOCTYPE html>
<html lang="en">
<head>
<meta charset="utf-8">
<title>Kiro Harbour Limited – Business Card</title>
<link rel="stylesheet" href="https://fonts.googleapis.com/css2?family=Open+Sans:wght@400;700&display=swap">
<style>
  :root {
    --backdrop: #4b403a;
    --card: #161616;
    --card-edge: #0c0c0c;
    --logo-faint: #4d4d4f;
    --text-light: #f2f2f2;
    --text-muted: #b9b9b9;
  }
  * { box-sizing: border-box; margin: 0; padding: 0; }
  html, body {
    width: 1200px;
    height: 715px;
    overflow: hidden;
    background: var(--backdrop);
    font-family: "Open Sans", sans-serif;
  }
  .canvas {
    position: relative;
    width: 1200px;
    height: 715px;
    display: flex;
    align-items: center;
    justify-content: center;
    gap: 40px;
  }
  .card {
    position: relative;
    width: 540px;
    height: 309px;
    background: var(--card);
    border: 1px solid var(--card-edge);
    box-shadow: 0 10px 24px rgba(0, 0, 0, 0.35);
    color: var(--text-light);
  }

  /* Front side */
  .card-front .wordmark {
    position: absolute;
    left: 0;
    right: 0;
    top: 50%;
    transform: translateY(-50%);
    text-align: center;
    font-weight: 700;
    font-size: 118px;
    letter-spacing: 4px;
    line-height: 1;
    color: var(--logo-faint);
  }

  /* Back side */
  .holder {
    position: absolute;
    left: 30px;
    top: 30px;
  }
  .holder-name {
    font-weight: 700;
    font-size: 15px;
    letter-spacing: 0.5px;
  }
  .holder-title {
    font-size: 10px;
    color: var(--text-muted);
    margin-top: 2px;
  }
  .card-back .wordmark {
    position: absolute;
    right: 34px;
    top: 104px;
    font-weight: 700;
    font-size: 70px;
    letter-spacing: 2px;
    line-height: 1;
    color: var(--text-light);
  }
  .contact-list {
    position: absolute;
    left: 30px;
    bottom: 30px;
    list-style: none;
    font-size: 12px;
    letter-spacing: 0.3px;
  }
  .contact-item {
    display: flex;
    align-items: center;
    gap: 8px;
    height: 18px;
  }
  .contact-icon {
    width: 12px;
    height: 12px;
    flex: none;
    fill: var(--text-light);
    stroke: var(--text-light);
  }
</style>
</head>
<body>
<main class="canvas">

  <section class="card card-front" aria-label="Card front">
    <div class="wordmark">KIRO</div>
  </section>

  <section class="card card-back" aria-label="Card back">
    <div class="holder">
      <p class="holder-name">Dorian Pallister</p>
      <p class="holder-title">Your Title</p>
    </div>

    <div class="wordmark">KIRO</div>

    <ul class="contact-list">
      <li class="contact-item">
        <svg class="contact-icon" viewBox="0 0 12 12" aria-hidden="true">
          <rect x="3" y="0.8" width="6" height="10.4" rx="1.2" fill="none" stroke-width="1.2"/>
          <circle cx="6" cy="9.3" r="0.7" stroke="none"/>
        </svg>
        <span>1 (212) 555-0143</span>
      </li>
      <li class="contact-item">
        <svg class="contact-icon" viewBox="0 0 12 12" aria-hidden="true">
          <path d="M1 4.5 C1 2 11 2 11 4.5 L9 5 L8.5 3.8 L3.5 3.8 L3 5 Z" stroke="none"/>
          <path d="M3 6 L9 6 L10.5 11 L1.5 11 Z" stroke="none"/>
          <circle cx="6" cy="8.3" r="1.2" fill="#161616" stroke="none"/>
        </svg>
        <span>1 (212) 555-0178</span>
      </li>
      <li class="contact-item">
        <svg class="contact-icon" viewBox="0 0 12 12" aria-hidden="true">
          <rect x="0.8" y="2.3" width="10.4" height="7.4" stroke="none"/>
          <path d="M0.8 2.5 L6 6.6 L11.2 2.5" fill="none" stroke="#161616" stroke-width="1"/>
        </svg>
        <span>dorian27@kiroharbour-mail.com</span>
      </li>
      <li class="contact-item">
        <svg class="contact-icon" viewBox="0 0 12 12" aria-hidden="true" fill="none" stroke-width="0.9">
          <circle cx="6" cy="6" r="5.2"/>
          <ellipse cx="6" cy="6" rx="2.2" ry="5.2"/>
          <path d="M0.8 6 H11.2 M1.6 3.4 H10.4 M1.6 8.6 H10.4"/>
        </svg>
        <span>www.kiroharbour-mail.com</span>
      </li>
      <li class="contact-item">
        <svg class="contact-icon" viewBox="0 0 12 12" aria-hidden="true">
          <path d="M6 11.5 C3.5 8 2.2 6.2 2.2 4.4 A3.8 3.8 0 0 1 9.8 4.4 C9.8 6.2 8.5 8 6 11.5 Z" stroke="none"/>
          <circle cx="6" cy="4.4" r="1.4" fill="#161616" stroke="none"/>
        </svg>
        <span>482 Halden Ave, New York, NY 10160, USA</span>
      </li>
    </ul>
  </section>

</main>
</body>
</html>
```